Gift Card and Gift Card Holder Design

Hello I need a design for a gift card and the gift card holder. I am uploading two PDFs for examples of designs we used for other promotional flyers. I am also uploading some design templates - two gift card holder templates (each would require the same design) and one gift card template. Also attached are two images of another gift card design - simple front, back had areas for text. We will need these areas for text in the design. We will provide copy for those areas but we should be able to edit following the close of the design project with you.

Font styles to use
Sans Serif

Colors
ec1f27
0455a3

Requirements
Must have
• use this web site for color reference: https://brqvantel.com/
• use this website for design inspiration for custom gift card holders: https://plumtessa.com/customgiftcardholder.html
• option with $75 on front of card as value
• two more options without

```html
<!DOCTYPE html>
<html lang="en">
<head>
<meta charset="utf-8">
<title>Gift Card Holder and Gift Card</title>
<link rel="stylesheet" href="https://fonts.googleapis.com/css2?family=Bebas+Neue&display=swap">
<style>
  :root {
    --page: #ffffff;
    --wood-light: #eeeeee;
    --wood-mid: #d6d6d6;
    --wood-seam: #2a2a2a;
    --gift-red: #9c1c23;
    --card-blue: #1f2f72;
    --ribbon-blue: #1f4fd6;
    --ribbon-shade: #1a3fb0;
    --dieline: #1a1a1a;
  }
  html, body {
    margin: 0;
    padding: 0;
    width: 1200px;
    height: 884px;
    overflow: hidden;
    background: var(--page);
  }
  .canvas {
    position: relative;
    width: 1200px;
    height: 884px;
  }
  .panel {
    position: absolute;
    top: 29px;
    width: 547px;
    height: 828px;
    overflow: hidden;
  }
  .panel--holder { left: 35px; }
  .panel--card { left: 623px; }
  .wood {
    position: absolute;
    inset: 0;
    background: linear-gradient(100deg, var(--wood-light) 0%, var(--wood-mid) 30%, var(--wood-light) 55%, var(--wood-mid) 80%, var(--wood-light) 100%);
  }
  .art {
    position: absolute;
    inset: 0;
  }
  .headline {
    position: absolute;
    margin: 0;
    font-family: "Bebas Neue", "Arial Narrow", sans-serif;
    font-weight: 400;
    line-height: 1;
    white-space: nowrap;
    filter: drop-shadow(3px 3px 2px rgba(0,0,0,0.45));
  }
  .headline .gift { color: var(--gift-red); }
  .headline .card { color: var(--card-blue); }
  .panel--holder .headline {
    left: 67px;
    top: 66px;
    font-size: 142px;
    letter-spacing: 2px;
  }
  .panel--card .headline {
    left: 42px;
    top: 368px;
    font-size: 156px;
    letter-spacing: 2px;
  }
  .brand-name {
    position: absolute;
    left: 0;
    right: 0;
    top: 150px;
    margin: 0;
    text-align: center;
    font-family: "Bebas Neue", "Arial Narrow", sans-serif;
    font-weight: 400;
    font-size: 120px;
    line-height: 1;
    color: var(--card-blue);
  }
</style>
</head>
<body>
<main class="canvas">

  <section class="panel panel--holder" aria-label="Gift card holder, back">
    <div class="wood" role="img" aria-label="Whitewashed grey wood plank texture"></div>
    <svg class="art" width="547" height="828" viewBox="0 0 547 828">
      <line class="plank-seam" x1="357" y1="0" x2="357" y2="828" stroke="var(--wood-seam)" stroke-width="3"/>
      <polygon class="ribbon" points="0,596 547,708 547,765 0,654" fill="var(--ribbon-blue)"/>
      <polygon class="ribbon-edge" points="0,640 547,752 547,765 0,654" fill="var(--ribbon-shade)"/>
      <polyline class="dieline" points="4,0 27,285 522,285 544,0" fill="none" stroke="var(--dieline)" stroke-width="1"/>
      <path class="dieline-thumb" d="M149,327 Q276,162 404,327" fill="none" stroke="var(--dieline)" stroke-width="1"/>
    </svg>
    <h2 class="headline"><span class="gift">GIFT</span> <span class="card">CARD</span></h2>
  </section>

  <section class="panel panel--card" aria-label="Gift card holder, front">
    <div class="wood" role="img" aria-label="Whitewashed grey wood plank texture"></div>
    <svg class="art" width="547" height="828" viewBox="0 0 547 828">
      <line class="plank-seam" x1="184" y1="0" x2="184" y2="828" stroke="var(--wood-seam)" stroke-width="3"/>
      <line class="plank-seam" x1="545" y1="0" x2="545" y2="828" stroke="var(--wood-seam)" stroke-width="2"/>
      <polygon class="ribbon" points="0,708 547,593 547,651 0,765" fill="var(--ribbon-blue)"/>
      <polygon class="ribbon-edge" points="0,752 547,638 547,651 0,765" fill="var(--ribbon-shade)"/>
      <ellipse class="bow" cx="280" cy="680" rx="135" ry="92" fill="var(--ribbon-blue)" role="img" aria-label="Satin ribbon bow illustration"/>
    </svg>
    <p class="brand-name">Brqvantel</p>
    <h2 class="headline"><span class="gift">GIFT</span> <span class="card">CARD</span></h2>
  </section>

</main>
</body>
</html>
```